2 page Web Site Design (Coded), simple, not picky

I need a web portal for a PPC marketing business. I have the logo, some imagery, and some websites to base the design on.

***Background***
The name of the business is "Quiet Harbor Outreach Advisors" or QHOA. We provide listings in a searchable database for Dental Sleep Medicine doctors. These are doctors who treat snoring/sleep apnea/and CPAP users with oral appliances. Client doctors will have their own "landing page website" where PPC prospects land from the PPC campaigns. Logos for supporting/landing page websites have been uploaded.
***End Background***

THIS website (for you to design) is to introduce doctors to the concept and detail the services. i.e. PPC campaign management services, listing on a national database of Dental Sleep Medicine practitioners, and a fully featured website dedicated to Snoring, Sleep Apnea, and CPAP Alternative treatment (those websites are "Farewell-Rumble.com", "Farewell-NightGasp.com", and ""Farewell-MaskTube.com")

SEM websites whose look I enjoy are:

http://www.brindlequay.com/marketing-services/pay-per-click/

http://www.orchardvantage.com/welcome/pay-per-click-services/

http://www.lanternpeak.com/marketing-services/paid-search-management/

The main colors are Red, White, & Blue. Red and blue used mostly for accents/emphasis.

The main/index page's purpose is to, as best possible, convey the idea of SEM campaign management with supporting websites being their best option for internet marketing!
The secondary page is just a slightly modified layout where details can be explained.

Target Market(s)

Dentists who practice Dental Sleep Medicine (see www.rqtvo.org)

Industry/Entity Type

Marketing

Requirements
Must have
• -Sign-up form for the generation of leads... Simple script that sends E-mail is fine... Doctor's Name, Business Name, Business Address, E-mail address, phone #.

-Graphics that will clearly describe the services being provided.

```html
<!DOCTYPE html>
<html lang="en">
<head>
<meta charset="utf-8">
<title>QHOA — Quiet Harbor Outreach Advisors</title>
<link rel="stylesheet" href="https://fonts.googleapis.com/css2?family=Oswald:wght@300;400&family=PT+Sans:wght@400;700&display=swap">
<style>
:root{
  --red:#b5212e;
  --blue:#3b4a9a;
  --navy:#1f3f8f;
  --ink:#3a3a3a;
  --muted:#666;
  --band:#ececec;
  --panel:#e0e0e0;
  --line:#dcdcdc;
  --dark:#555657;
  --white:#fff;
}
*{box-sizing:border-box;margin:0;padding:0}
html,body{width:1200px;height:840px;overflow:hidden;background:var(--white);font-family:"PT Sans",sans-serif;color:var(--ink)}
.page{position:relative;width:1200px;height:840px}
.top-bar{position:absolute;left:171px;top:0;width:858px;height:10px;background:var(--dark)}
.brand{position:absolute;left:173px;top:24px;display:flex;flex-direction:column}
.brand-row{display:flex;align-items:center;gap:8px}
.brand-mark{width:30px;height:30px;border-radius:50%;background:var(--navy)}
.brand-name{font-family:"Oswald",sans-serif;font-weight:400;font-size:38px;line-height:40px;color:var(--red);letter-spacing:1px}
.brand-tagline{font-weight:700;font-size:11px;color:var(--red);margin-top:4px}
.main-nav{position:absolute;right:171px;top:46px;display:flex;gap:24px;font-family:"Oswald",sans-serif;font-weight:300;font-size:13px;letter-spacing:1px;color:#777}
.main-nav .active{color:var(--red)}
.hero{position:absolute;left:0;top:103px;width:1200px;height:304px;background:var(--band)}
.hero-copy{position:absolute;left:182px;top:22px;width:530px}
.hero-title{font-family:"Oswald",sans-serif;font-weight:300;font-size:40px;line-height:48px;letter-spacing:3px;color:#444}
.hero-title span{display:block;white-space:nowrap}
.hero-text{margin-top:12px;width:440px;font-size:12px;line-height:22px;letter-spacing:.8px;color:#444}
.hero-list{list-style:none;margin-top:12px}
.hero-list li{position:relative;padding-left:17px;font-weight:700;font-size:10.5px;letter-spacing:.8px;color:var(--blue);line-height:29px;white-space:nowrap}
.hero-list li::before{content:"";position:absolute;left:2px;top:10px;border-left:7px solid var(--red);border-top:4px solid transparent;border-bottom:4px solid transparent}
.lead-form{position:absolute;left:722px;top:0;width:293px;height:304px;background:var(--panel);padding-top:28px;text-align:center}
.lead-form h2{font-family:"Oswald",sans-serif;font-weight:300;font-size:19px;letter-spacing:1px;color:#444}
.field{display:block;width:252px;height:32px;margin:0 auto;border:1px solid #bbb;background:var(--white);padding-left:10px;text-align:left;font-style:italic;font-size:11.5px;letter-spacing:1px;color:#666;line-height:30px}
.field-name{margin-top:19px}
.field-email{margin-top:21px}
.field-phone{margin-top:24px}
.submit{display:block;width:120px;height:39px;margin:27px auto 0;background:var(--red);color:var(--white);font-family:"Oswald",sans-serif;font-weight:300;font-size:18px;letter-spacing:1px;line-height:39px}
.features{position:absolute;left:171px;top:422px;width:858px;height:359px;border:1px solid var(--line)}
.card{position:absolute;top:27px;width:244px;height:304px;border:1px solid var(--line);border-radius:4px;box-shadow:0 1px 3px rgba(0,0,0,.08);background:var(--white);overflow:hidden}
.card-1{left:23px}.card-2{left:308px}.card-3{left:589px}
.card-head{height:38px;background:#f0f0f0;display:flex;align-items:center;gap:10px;padding-left:18px;font-family:"Oswald",sans-serif;font-weight:300;font-size:13.5px;letter-spacing:1px;color:#333}
.card-head svg{width:22px;height:22px;fill:#666}
.card-text{padding:13px 15px 0;height:94px;font-size:11.5px;line-height:19px;letter-spacing:.4px;color:#555}
.card-photo{height:124px}
.photo-desk{background:linear-gradient(135deg,#f2f2f2,#cfd2d6 60%,#8a8d92)}
.photo-screen{background:linear-gradient(180deg,#f4f4f4,#c9cbd0)}
.photo-rest{background:linear-gradient(120deg,#b9785a,#e8c9b4 55%,#f3f0ee)}
.more{display:block;width:70px;height:27px;margin:11px auto 0;background:var(--red);color:var(--white);text-align:center;font-family:"Oswald",sans-serif;font-weight:300;font-size:13px;letter-spacing:1px;line-height:27px}
.footer{position:absolute;left:0;top:796px;width:1200px;height:44px;background:var(--dark);color:#eee;font-size:9px;letter-spacing:.5px}
.footer-copy{position:absolute;left:171px;top:18px}
.footer-nav{position:absolute;right:171px;top:18px;display:flex;gap:16px}
.footer-nav .active{color:#222}
</style>
</head>
<body>
<div class="page">
  <div class="top-bar"></div>

  <header>
    <div class="brand">
      <div class="brand-row"><span class="brand-mark"></span><span class="brand-name">QHOA</span></div>
      <span class="brand-tagline">Quiet Harbor Outreach Advisors</span>
    </div>
    <nav class="main-nav">
      <span class="active">HOME</span><span>SERVICES</span><span>CLIENTS</span><span>ABOUT</span><span>BLOG</span><span>CONTACT US</span>
    </nav>
  </header>

  <section class="hero">
    <div class="hero-copy">
      <h1 class="hero-title"><span>Lorem ipsum dolor sit amet</span><span>consectetur adipis allet</span></h1>
      <p class="hero-text">Nam est ante, condimentum eu rhoncus sed, egestas a turpis. Phasellus laoreet aliquet odio vitae adipiscing nullam hendrerit dignissim augue .</p>
      <ul class="hero-list">
        <li>Integer suscipit consequat luctus ellen yellor thenrede illenetery ulle</li>
        <li>Nunc vel purus quam &nbsp;leo convallis id faseter girtey loenerret utlietre</li>
        <li>Vestibulum molestie fermentum purus, et sodales oppertte ono</li>
      </ul>
    </div>
    <form class="lead-form">
      <h2>LOREM IPSUM DOLOR AMET</h2>
      <span class="field field-name">Your Name</span>
      <span class="field field-email">Your Email</span>
      <span class="field field-phone">Your Phone Number</span>
      <span class="submit">SUBMIT</span>
    </form>
  </section>

  <section class="features">
    <article class="card card-1">
      <div class="card-head">
        <svg viewBox="0 0 24 24"><circle cx="12" cy="12" r="7"/><circle cx="12" cy="12" r="9.5" fill="none" stroke="#666" stroke-width="3" stroke-dasharray="3 2.2"/><circle cx="12" cy="12" r="3" fill="#f0f0f0"/></svg>
        LOREM IPSUM CENTARINOS
      </div>
      <p class="card-text">Cras vel velit mauris. Proin et odio eu dui euismod congue eget et neque. Maecenas lectus magna, dignissim et varius vitae heetore.</p>
      <div class="card-photo photo-desk" role="img" aria-label="Photo of a hand on a computer mouse beside a keyboard"></div>
      <span class="more">MORE</span>
    </article>
    <article class="card card-2">
      <div class="card-head">
        <svg viewBox="0 0 24 24"><circle cx="12" cy="9" r="6" fill="none" stroke="#666" stroke-width="2.5"/><rect x="9" y="16" width="6" height="2.5"/><rect x="9.5" y="19.5" width="5" height="2.5"/></svg>
        LOREM IPSUM DOLOMBER
      </div>
      <p class="card-text">Cras vel velit mauris. Proin et odio eu dui euismod congue eget et neque. Maecenas lectus magna, dignissim et varius vitae heetore.</p>
      <div class="card-photo photo-screen" role="img" aria-label="Desktop monitor showing search results with paid ads highlighted"></div>
      <span class="more">MORE</span>
    </article>
    <article class="card card-3">
      <div class="card-head">
        <svg viewBox="0 0 24 24"><circle cx="12" cy="7" r="5"/><path d="M2 23c0-6 4-9 10-9s10 3 10 9z"/></svg>
        ELLEMBERING NOUANED
      </div>
      <p class="card-text">Cras vel velit mauris. Proin et odio eu dui euismod congue eget et neque. Maecenas lectus magna, dignissim et varius vitae heetore.</p>
      <div class="card-photo photo-rest" role="img" aria-label="Photo of a person resting peacefully on a pillow"></div>
      <span class="more">MORE</span>
    </article>
  </section>

  <footer class="footer">
    <span class="footer-copy">Copyright ©2012 All rights reserved</span>
    <nav class="footer-nav"><span class="active">Home</span><span>Services</span><span>Clients</span><span>About</span><span>Blog</span><span>Contact Us</span></nav>
  </footer>
</div>
</body>
</html>
```